The Book Cover for "Finding the Silver Lantern of Dawn" needs redesigned

First the back ground or art work needs to be replaced or redesigned.
The title Finding the Silver Lantern of Dawn needs to be redesigned so that the words "Finding the" is diminished in size compared to the rest of the title "Silver Lantern of Dawn"
The Sub-title "Tracing the forgotten path of the Evening Wind" needs to be more pronounced and readable.
The authors name needs to be downsized.

```html
<!DOCTYPE html>
<html lang="en">
<head>
<meta charset="utf-8">
<title>Finding the Silver Lantern of Dawn</title>
<link rel="stylesheet" href="https://fonts.googleapis.com/css2?family=Cinzel:wght@400;500;600;700&display=swap">
<style>
  :root {
    --title-plum: #4a0a42;
    --sky-white: #ffffff;
    --mist: #eef2e4;
    --leaf-light: #9bbf78;
    --meadow: #5f8a3e;
    --meadow-mid: #3f6328;
    --meadow-deep: #22361a;
    --text-light: #ffffff;
    --text-shade: rgba(10, 20, 6, 0.75);
  }
  html, body {
    margin: 0;
    padding: 0;
    width: 800px;
    height: 1200px;
    overflow: hidden;
    background: var(--sky-white);
  }
  .cover {
    position: relative;
    width: 800px;
    height: 1200px;
    overflow: hidden;
    font-family: "Cinzel", "Times New Roman", serif;
  }
  .cover-art {
    position: absolute;
    inset: 0;
    background:
      radial-gradient(ellipse 70% 25% at 50% 40%, rgba(255,255,255,0.95), rgba(255,255,255,0) 70%),
      linear-gradient(180deg,
        var(--sky-white) 0%,
        var(--sky-white) 30%,
        var(--mist) 40%,
        var(--leaf-light) 50%,
        #7f9e68 57%,
        var(--meadow) 66%,
        var(--meadow-mid) 78%,
        var(--meadow-deep) 100%);
  }
  .cover-type {
    position: absolute;
    inset: 0;
    width: 800px;
    height: 1200px;
  }
  .title-lead, .title-main {
    fill: var(--title-plum);
    font-weight: 500;
  }
  .subtitle {
    fill: var(--text-light);
    font-weight: 700;
    filter: drop-shadow(0 2px 3px var(--text-shade));
  }
  .author {
    fill: var(--text-light);
    font-weight: 600;
    filter: drop-shadow(0 1px 2px var(--text-shade));
  }
</style>
</head>
<body>
  <main class="cover">
    <div class="cover-art" role="img" aria-label="Misty meadow at dawn with sunlit trees and a woman in a purple dress holding a baby in the foreground"></div>
    <svg class="cover-type" viewBox="0 0 800 1200" xmlns="http://www.w3.org/2000/svg">
      <text class="title-lead" x="113" y="100" font-size="56" textLength="580" lengthAdjust="spacingAndGlyphs">FINDING THE</text>
      <text class="title-main" x="100" y="224" font-size="122" textLength="605" lengthAdjust="spacingAndGlyphs">SILVER</text>
      <text class="title-main" x="100" y="375" font-size="118" textLength="602" lengthAdjust="spacingAndGlyphs">LANTERN</text>
      <text class="title-main" x="100" y="520" font-size="118" textLength="605" lengthAdjust="spacingAndGlyphs">OF DAWN</text>
      <text class="subtitle" x="112" y="1040" font-size="46" textLength="580" lengthAdjust="spacingAndGlyphs">TRACING THE FORGOTTEN</text>
      <text class="subtitle" x="48" y="1100" font-size="46" textLength="707" lengthAdjust="spacingAndGlyphs">PATH OF THE EVENING WIND</text>
      <text class="author" x="230" y="1166" font-size="24" textLength="340" lengthAdjust="spacingAndGlyphs">H. W. REED RAVENSCROFT</text>
    </svg>
  </main>
</body>
</html>
```